Design Book Cover - Win The Hiring Room

Need assistance designing a compelling cover for an eBook titled "Win The Hiring Room". eBook is a hard hitting, direct tutorial for how to succeed in a job interview. Written by Derek Pollfrey, a senior partner with 20 years interviewing people for employment at one of the largest and most prestigious consulting firms in the world.

Target Market(s)

anyone looking to land a corporate job with Summit 1000 companies

Industry/Entity Type

Consulting

```html
<!DOCTYPE html>
<html lang="en">
<head>
<meta charset="UTF-8">
<title>Win The Hiring Room — Derek Pollfrey</title>
<link rel="stylesheet" href="https://fonts.googleapis.com/css2?family=Open+Sans:wght@800&family=Cinzel:wght@400&display=swap">
<style>
  :root {
    --bg-dark: #141414;
    --bg-mid: #3a3a3a;
    --title-white: #ffffff;
    --title-blue: #c3daf2;
    --rule-white: #ffffff;
    --photo-navy: #0f2148;
    --photo-blue: #2f5aa8;
    --photo-light: #eef7fd;
  }
  html, body {
    margin: 0;
    padding: 0;
    width: 750px;
    height: 1200px;
    overflow: hidden;
    background: var(--bg-dark);
  }
  .cover {
    position: relative;
    width: 750px;
    height: 1200px;
    overflow: hidden;
    background: radial-gradient(ellipse 70% 45% at 50% 22%, var(--bg-mid) 0%, var(--bg-dark) 85%);
  }
  .cover__art {
    position: absolute;
    inset: 0;
    width: 750px;
    height: 1200px;
  }
  .title-line {
    font-family: "Open Sans", Arial, sans-serif;
    font-weight: 800;
  }
  .title-line--top { fill: var(--title-white); }
  .title-line--bottom { fill: var(--title-blue); }
  .title-rule { fill: var(--title-blue); }
  .photo-frame { fill: var(--rule-white); }
  .author-name {
    font-family: "Cinzel", "Times New Roman", serif;
    font-weight: 400;
    fill: var(--title-white);
  }
</style>
</head>
<body>
  <main class="cover">
    <svg class="cover__art" viewBox="0 0 750 1200" xmlns="http://www.w3.org/2000/svg">
      <defs>
        <linearGradient id="photoTone" x1="0" y1="0" x2="1" y2="0">
          <stop offset="0" stop-color="var(--photo-navy)"/>
          <stop offset="0.18" stop-color="var(--photo-blue)"/>
          <stop offset="0.45" stop-color="var(--photo-light)"/>
          <stop offset="0.62" stop-color="var(--photo-light)"/>
          <stop offset="0.85" stop-color="var(--photo-blue)"/>
          <stop offset="1" stop-color="var(--photo-navy)"/>
        </linearGradient>
      </defs>

      <g class="title">
        <text class="title-line title-line--top" x="60" y="212" font-size="168" textLength="636" lengthAdjust="spacingAndGlyphs">WIN THE</text>
        <text class="title-line title-line--bottom" x="58" y="375" font-size="162" textLength="638" lengthAdjust="spacingAndGlyphs">HIRING ROOM</text>
        <rect class="title-rule" x="52" y="404" width="644" height="8"/>
      </g>

      <g class="photo">
        <rect class="photo-frame" x="0" y="476" width="750" height="572"/>
        <rect x="0" y="483" width="750" height="557" fill="url(#photoTone)" role="img" aria-label="Photo of two business people in dark suits shaking hands against a bright office background"/>
      </g>

      <text class="author-name" x="82" y="1150" font-size="72" textLength="610" lengthAdjust="spacingAndGlyphs">DEREK POLLFREY</text>
    </svg>
  </main>
</body>
</html>
```